Judicial election website to attract voters

I need a simple one-page web design for a judicial election. I'm going to put up one picture, maybe two. The picture I have needs a little touch-up (whiten teeth for example). I have 3 paragraphs of text. I'd like a "Donate" button that can link to a CoinDrift account. I'd also like a little background design, like the Constitution or something like that. There's a couple other little things but that's the bulk of it.

Target Market(s)

Involved voters and some media

Industry/Entity Type

Legal

Number of Pages Required

1 page

Font styles to use
Sans Serif

Requirements
Must have
• My picture, text, donate button
• Phrase "Remember to vote August 30, 2016!"
Nice to have
• Perhaps a second photo, maybe a short 30 second video of me talking directly to the voters, cool background: Constitution, something judgey.
Should not have
• Not sure ... profanity, I guess.

```html
<!DOCTYPE html>
<html lang="en">
<head>
<meta charset="utf-8">
<title>Judicial Election</title>
<link href="https://fonts.googleapis.com/css2?family=Cabin+Condensed:wght@400;500;600;700&display=swap" rel="stylesheet">
<style>
:root{
  --navy:#2c3e50;
  --blue:#2d86c4;
  --red:#e74c3c;
  --red-dark:#b8382b;
  --text:#3d3d3d;
  --white:#ffffff;
  --page:#c9cdd0;
}
*{margin:0;padding:0;box-sizing:border-box}
html,body{width:995px;height:1200px;overflow:hidden}
body{
  position:relative;
  font-family:"Cabin Condensed",sans-serif;
  color:var(--text);
  background:linear-gradient(180deg,#5b5e62 0%,#9a9da0 22%,#d3d6d8 50%,#d9dcde 100%);
}
.site-header{
  position:absolute;left:61px;top:27px;width:873px;height:77px;
  background:var(--white);border-radius:6px 6px 0 0;
}
.brand{
  position:absolute;left:24px;top:22px;font-size:28px;font-weight:600;
  color:var(--navy);letter-spacing:-.3px;
}
.brand span{color:var(--blue)}
.main-nav{position:absolute;left:311px;top:31px;display:flex;gap:37px}
.main-nav a{font-size:17px;font-weight:600;color:var(--navy);text-decoration:none}
.social{position:absolute;right:15px;top:25px;display:flex;gap:6px}
.social span{width:29px;height:29px;border-radius:50%;background:var(--blue);display:block}
.hero{
  position:absolute;left:61px;top:103px;width:873px;height:468px;
  border-radius:0 0 6px 6px;overflow:hidden;
  background:linear-gradient(180deg,#8fa0b8 0%,#d8a4a7 30%,#c65a5e 55%,#8c7f86 75%,#5a6a72 100%);
}
.vote-banner{
  position:absolute;left:254px;top:472px;width:487px;height:55px;
  background:var(--blue);border-radius:6px;color:var(--white);
  font-size:20px;font-weight:600;
}
.vote-banner .left{position:absolute;left:44px;top:14px}
.vote-banner .right{position:absolute;right:33px;top:14px}
.vote-badge{position:absolute;left:428px;top:425px;width:140px;height:140px}
.bio-card{
  position:absolute;left:61px;top:618px;width:873px;height:514px;
  background:linear-gradient(90deg,#ffffff 0%,#ffffff 35%,#f1f2f3 60%,#fafafa 100%);
  border-radius:6px;box-shadow:0 0 3px rgba(0,0,0,.15);
}
.portrait{
  position:absolute;left:76px;top:582px;width:276px;height:282px;
  border-radius:50%;border-top:4px solid var(--navy);
  background:radial-gradient(circle at 50% 45%,#d79b86 0%,#c9ab84 45%,#e3e6e4 80%);
}
.bio-text{
  position:absolute;left:379px;top:649px;width:535px;
  font-size:12.6px;line-height:23px;color:var(--text);
}
.bio-text p{margin-bottom:23px}
.donate{
  position:absolute;left:90px;top:1032px;width:244px;height:65px;
  background:var(--red);border-radius:7px;border-bottom:4px solid var(--red-dark);
  color:var(--white);font-size:29px;font-weight:600;text-align:center;
  line-height:61px;text-decoration:none;
}
.site-footer{
  position:absolute;left:0;top:1164px;width:995px;height:36px;
  background:var(--navy);color:var(--white);font-size:12.5px;
  text-align:center;line-height:36px;
}
</style>
</head>
<body>
<header class="site-header">
  <div class="brand">JUDICIAL <span>ELECTION</span></div>
  <nav class="main-nav"><a href="#">EXPERIENCED</a><a href="#">DEDICATED</a><a href="#">RESPECTED</a></nav>
  <div class="social" aria-label="Social links"><span></span><span></span><span></span><span></span></div>
</header>

<div class="hero" role="img" aria-label="American flag waving over a city skyline at sunset reflected in a river"></div>

<div class="vote-banner"><span class="left">REMEMBER TO</span><span class="right">AUGUST 30, 2016!</span></div>
<svg class="vote-badge" viewBox="0 0 140 140" aria-label="Vote badge">
  <circle cx="70" cy="70" r="68" fill="var(--blue)"/>
  <circle cx="70" cy="70" r="58" fill="var(--white)"/>
  <circle cx="70" cy="70" r="53" fill="var(--blue)"/>
  <text x="70" y="84" text-anchor="middle" font-family="Cabin Condensed, sans-serif" font-weight="700" font-size="40" fill="var(--white)">VOTE!</text>
</svg>

<section class="bio-card"></section>
<div class="portrait" role="img" aria-label="Portrait photo of the candidate"></div>

<div class="bio-text">
  <p>Marianne was born and raised in Tampa Florida, the daughter of an air-conditioning repairman who later opened his own successful business. As the first in her family to go to college, her parents could not have been more proud as she finished her degree at Gulf Coast University, then continued on to Capitol State School of Law where she graduated with honors.</p>
  <p>Dedicating her life to public service in central Florida, she has spent the last 18 years as a prosecutor fighting for victims of child abuse and sexual abuse in Orange and Osceola counties. She participates in local charities such as the Harvest Table Pantry and the Open Pages Reading League. Marianne shares her knowledge and experience freely, often mentoring the other young prosecutors and lecturing on jury selection and trial strategies. She is also committed to ensuring ethical behavior in the profession of law. In law school, she won an award for ethics and professionalism but since then she also served as Chair of a State Bar Grievance Committee, which handles complaints and ethical violations committed by local attorneys.</p>
  <p>The cornerstone of Marianne's candidacy for judge is her experience in the courtroom. Nobody knows how to run an efficient courtroom better than an attorney who has litigated a hundred felony jury trials and argued more pretrial motions than can be counted. But even a judge with all the right knowledge and experience cannot excel without the correct temperament. Ask any attorney or judge who has worked with Marianne and they will tell you that she treats everyone with respect and handles courtroom surprises with a calm head and sense of humor. She would love your support for judge and the opportunity to use her skills and experience to serve Orange and Osceola County in a new and exciting way.</p>
</div>

<a class="donate" href="#" aria-label="Donate via CoinDrift">DONATE NOW!</a>

<footer class="site-footer">Copyright © 2016 Judicial Election.</footer>
</body>
</html>
```